diesel mechanic business card design

summit diesel is a new and upcoming business we are looking for some bad ass designs to help get us started we offer 24 hour road service, off road recovery, welding and custom fabrications we are diesel mechanics so our design should be bold and eye catching flames wrenches engine parts are cool we work in an industrial environment around heavy trucks and equipment this in not a quikko oil we fix it all nothing is to big or to small the colors red and black are always a plus but we are open to anything you guys can come up with ready set go

Target Market(s)

other small business primarily trucking and transportation companys

Industry/Entity Type

Business

Contact Information for Business Card

company name Sumitt diesel truck & trailer repair / address 14 rear north holbrin ave corwell ND 58999 / ownersAdam DeLuccie 570-555-0143 / Curtis Lavandel 570-555-0178 E mail brentmarvoski@mailvex.com fax 570-555-0192

Requirements
Nice to have
• industrial modern design
Should not have
• rainbows butterfly's unicorns or cupcakes

```html
<!DOCTYPE html>
<html lang="en">
<head>
<meta charset="utf-8">
<title>Sumitt Diesel Business Card</title>
<link href="https://fonts.googleapis.com/css2?family=Questrial&display=swap" rel="stylesheet">
<style>
  :root {
    --page-bg: #ebebeb;
    --card-bg: #333335;
    --accent-blue: #1f93d8;
    --text-white: #f4f4f4;
    --card-shadow: rgba(0, 0, 0, 0.28);
  }
  * { box-sizing: border-box; margin: 0; padding: 0; }
  html, body {
    width: 1200px;
    height: 1000px;
    overflow: hidden;
    background: var(--page-bg);
    font-family: "Questrial", "Century Gothic", sans-serif;
  }
  .canvas {
    width: 1200px;
    height: 1000px;
    display: flex;
    align-items: center;
    justify-content: center;
    gap: 48px;
  }
  .card {
    position: relative;
    width: 546px;
    height: 312px;
    background: var(--card-bg);
    box-shadow: 0 10px 26px var(--card-shadow);
    overflow: hidden;
    color: var(--text-white);
  }

  /* Front: contact side */
  .card-front { padding: 24px 26px; }
  .owners-label {
    text-align: right;
    font-size: 25px;
    letter-spacing: 1px;
    text-transform: uppercase;
    line-height: 1;
  }
  .owner-list { margin-top: 4px; }
  .owner {
    font-size: 27px;
    text-transform: uppercase;
    line-height: 1.1;
    white-space: nowrap;
  }
  .owner-phone { color: var(--accent-blue); }
  .contact-list { margin-top: 12px; }
  .contact-row {
    display: flex;
    align-items: center;
    gap: 6px;
    font-size: 19px;
    line-height: 1.45;
    white-space: nowrap;
  }
  .contact-label {
    background: var(--accent-blue);
    color: var(--text-white);
    padding: 0 6px;
    border-radius: 2px;
    font-size: 18px;
    line-height: 1.3;
  }
  .contact-email { font-size: 21px; }
  .corner-brand {
    position: absolute;
    right: 24px;
    bottom: 18px;
    display: flex;
    align-items: center;
    gap: 8px;
    color: var(--accent-blue);
    font-size: 14px;
    text-transform: uppercase;
    letter-spacing: 0.5px;
  }
  .corner-brand .brand-dot {
    width: 24px;
    height: 24px;
    border-radius: 50%;
    background: var(--accent-blue);
  }

  /* Back: brand side */
  .card-back {
    display: flex;
    flex-direction: column;
    align-items: center;
    justify-content: center;
    gap: 16px;
  }
  .back-brand-dot {
    width: 52px;
    height: 52px;
    border-radius: 50%;
    background: var(--accent-blue);
  }
  .back-brand-name {
    color: var(--accent-blue);
    font-size: 24px;
    text-transform: uppercase;
    letter-spacing: 1.5px;
    text-align: center;
    line-height: 1.3;
  }
</style>
</head>
<body>
  <main class="canvas">
    <section class="card card-front" aria-label="Business card contact side">
      <p class="owners-label">Owners</p>
      <div class="owner-list">
        <p class="owner">Brent Marvoski <span class="owner-phone">570-555-0143</span></p>
        <p class="owner">Curtis Lavandel <span class="owner-phone">570-555-0178</span></p>
      </div>
      <div class="contact-list">
        <p class="contact-row"><span class="contact-label">address</span>14 rear north holbrin ave corwell ND 58999</p>
        <p class="contact-row"><span class="contact-label">fax</span>570-555-0192</p>
        <p class="contact-row contact-email"><span class="contact-label">E mail</span>brentmarvoski@mailvex.com</p>
      </div>
      <div class="corner-brand">
        <span class="brand-dot"></span>
        <span>Sumitt diesel truck</span>
      </div>
    </section>

    <section class="card card-back" aria-label="Business card brand side">
      <span class="back-brand-dot"></span>
      <p class="back-brand-name">Sumitt diesel<br>truck &amp; trailer repair</p>
    </section>
  </main>
</body>
</html>
```